Australia rare honey label

Australia honey brand: Kelunto honey (dostwin rare honey)
Honey type: Red Gum, Orange bloosom, Black honey, Quince etc
Require obvious color or symble to distingwish above different type or taste

Target Market(s)

preminum customers

Font styles to use
Decorative
Script

Requirements
Nice to have
• unique idea which is not similar to market other honey brands.
There is a label sample reference for some information if want to know what infor need to be filled into labels

```html
<!DOCTYPE html>
<html lang="en">
<head>
<meta charset="utf-8">
<title>Kelunto Honey – Label Range</title>
<link href="https://fonts.googleapis.com/css2?family=Norican&family=Oswald:wght@600&family=Roboto:wght@400;700&display=swap" rel="stylesheet">
<style>
  :root {
    --canvas: #ffffff;
    --sage: #9db585;
    --sage-light: #dfe9d4;
    --sage-deep: #7f9d68;
    --paper: #fbfcf9;
    --script: #b2461a;
    --amber: #e8891c;
    --ink: #2f3a28;
    --comb: #c9ccc8;
    --red-gum: #e02a2f;
    --orange-blossom: #f08a4b;
    --black-honey: #6b2a1e;
    --quince: #e3d25a;
  }
  * { box-sizing: border-box; margin: 0; padding: 0; }
  html, body { width: 1200px; height: 565px; overflow: hidden; background: var(--canvas); }
  .range {
    position: relative; width: 1200px; height: 565px;
    display: flex; justify-content: center; align-items: center; gap: 22px;
  }
  .label {
    position: relative; width: 270px; height: 400px; overflow: hidden;
    background: linear-gradient(180deg, var(--sage-light) 0%, var(--paper) 30%, var(--paper) 100%);
    font-family: "Roboto", Arial, sans-serif; color: var(--ink);
    box-shadow: 0 2px 8px rgba(0,0,0,.12);
  }
  .label__top {
    position: absolute; left: 0; top: 0; width: 100%; height: 34px;
    background: linear-gradient(90deg, var(--sage) 0%, var(--sage-light) 50%, var(--sage) 100%);
  }
  .brand-mark {
    position: absolute; top: 48px; left: 50%; transform: translateX(-50%);
    display: flex; flex-direction: column; align-items: center; gap: 4px;
  }
  .brand-mark__dot {
    width: 30px; height: 30px; border-radius: 50%; background: var(--amber);
  }
  .brand-mark__name {
    background: var(--sage); padding: 2px 6px; text-align: center;
    font-size: 6px; line-height: 1.3; color: var(--ink); letter-spacing: .3px;
  }
  .comb {
    position: absolute; left: 88px; top: 118px; width: 94px; height: 150px;
    background: radial-gradient(ellipse at center, rgba(201,204,200,.45) 0%, rgba(201,204,200,0) 70%);
  }
  .title {
    position: absolute; left: 0; width: 100%; top: 150px; text-align: center;
    font-family: "Norican", cursive; color: var(--script); line-height: .9;
  }
  .title__brand { display: block; font-size: 44px; transform: translateX(-8px); }
  .title__word { display: block; font-size: 38px; transform: translateX(18px); }
  .drops {
    position: absolute; left: 50%; top: 252px; transform: translateX(-50%);
  }
  .side-copy {
    position: absolute; top: 40px; width: 34px; height: 205px;
    writing-mode: vertical-rl; transform: rotate(180deg);
    font-size: 5.2px; line-height: 1.35; font-style: italic; color: var(--ink);
  }
  .side-copy--left { left: 4px; }
  .side-copy--right { right: 4px; }
  .variety {
    position: absolute; left: 0; top: 288px; width: 100%; height: 32px;
    display: flex; align-items: center; justify-content: center;
    font-family: "Oswald", sans-serif; font-weight: 600; font-size: 19px; color: #fff;
    letter-spacing: .3px;
  }
  .variety--red-gum { background: linear-gradient(90deg, transparent 18%, var(--red-gum) 26%, var(--red-gum) 74%, transparent 84%); }
  .variety--orange-blossom { background: linear-gradient(90deg, transparent 18%, var(--orange-blossom) 26%, var(--orange-blossom) 74%, transparent 84%); }
  .variety--black-honey { background: linear-gradient(90deg, transparent 18%, var(--black-honey) 26%, var(--black-honey) 74%, transparent 84%); }
  .variety--quince { background: linear-gradient(90deg, transparent 18%, var(--quince) 26%, var(--quince) 74%, transparent 84%); }
  .label__bottom {
    position: absolute; left: 0; top: 320px; width: 100%; height: 72px;
    background: linear-gradient(90deg, var(--sage-deep) 0%, var(--sage) 50%, var(--sage-deep) 100%);
    padding: 10px 14px 0; text-align: center; font-size: 5.6px; line-height: 1.5; color: var(--ink);
  }
  .label__edge {
    position: absolute; left: 0; bottom: 0; width: 100%; height: 8px;
    background: linear-gradient(180deg, var(--amber) 0 2px, var(--sage-light) 2px);
  }
</style>
</head>
<body>
<main class="range">

  <article class="label">
    <div class="label__top"></div>
    <p class="side-copy side-copy--left">Raw honey gathered from native Australian blossoms, cold extracted and unfiltered to keep pollen and enzymes intact.</p>
    <p class="side-copy side-copy--right">Store below 25°C in a dry place. Natural crystallisation may occur; warm gently to restore. Not suitable for infants under twelve months.</p>
    <div class="brand-mark"><span class="brand-mark__dot"></span><span class="brand-mark__name">AUSTRALIA<br>KELUNTO HONEY</span></div>
    <div class="comb" role="img" aria-label="Faint honeycomb pattern behind the title"></div>
    <h2 class="title"><span class="title__brand">Kelunto</span><span class="title__word">Honey</span></h2>
    <svg class="drops" width="24" height="36" viewBox="0 0 24 36" aria-hidden="true"><path d="M6 0 C8 5 10 8 10 11 A4 4 0 0 1 2 11 C2 8 4 5 6 0Z" fill="var(--amber)"/><path d="M16 12 C19 19 22 22 22 27 A6 6 0 0 1 10 27 C10 22 13 19 16 12Z" fill="var(--amber)"/></svg>
    <div class="variety variety--red-gum">RED GUM</div>
    <p class="label__bottom">Pure Australian rare honey from dostwin apiaries, harvested in small batches each season. Net weight 500 g. Product of Australia.</p>
    <div class="label__edge"></div>
  </article>

  <article class="label">
    <div class="label__top"></div>
    <p class="side-copy side-copy--left">Raw honey gathered from native Australian blossoms, cold extracted and unfiltered to keep pollen and enzymes intact.</p>
    <p class="side-copy side-copy--right">Store below 25°C in a dry place. Natural crystallisation may occur; warm gently to restore. Not suitable for infants under twelve months.</p>
    <div class="brand-mark"><span class="brand-mark__dot"></span><span class="brand-mark__name">AUSTRALIA<br>KELUNTO HONEY</span></div>
    <div class="comb" role="img" aria-label="Faint honeycomb pattern behind the title"></div>
    <h2 class="title"><span class="title__brand">Kelunto</span><span class="title__word">Honey</span></h2>
    <svg class="drops" width="24" height="36" viewBox="0 0 24 36" aria-hidden="true"><path d="M6 0 C8 5 10 8 10 11 A4 4 0 0 1 2 11 C2 8 4 5 6 0Z" fill="var(--amber)"/><path d="M16 12 C19 19 22 22 22 27 A6 6 0 0 1 10 27 C10 22 13 19 16 12Z" fill="var(--amber)"/></svg>
    <div class="variety variety--orange-blossom">ORANGE BLOOSOM</div>
    <p class="label__bottom">Pure Australian rare honey from dostwin apiaries, harvested in small batches each season. Net weight 500 g. Product of Australia.</p>
    <div class="label__edge"></div>
  </article>

  <article class="label">
    <div class="label__top"></div>
    <p class="side-copy side-copy--left">Raw honey gathered from native Australian blossoms, cold extracted and unfiltered to keep pollen and enzymes intact.</p>
    <p class="side-copy side-copy--right">Store below 25°C in a dry place. Natural crystallisation may occur; warm gently to restore. Not suitable for infants under twelve months.</p>
    <div class="brand-mark"><span class="brand-mark__dot"></span><span class="brand-mark__name">AUSTRALIA<br>KELUNTO HONEY</span></div>
    <div class="comb" role="img" aria-label="Faint honeycomb pattern behind the title"></div>
    <h2 class="title"><span class="title__brand">Kelunto</span><span class="title__word">Honey</span></h2>
    <svg class="drops" width="24" height="36" viewBox="0 0 24 36" aria-hidden="true"><path d="M6 0 C8 5 10 8 10 11 A4 4 0 0 1 2 11 C2 8 4 5 6 0Z" fill="var(--amber)"/><path d="M16 12 C19 19 22 22 22 27 A6 6 0 0 1 10 27 C10 22 13 19 16 12Z" fill="var(--amber)"/></svg>
    <div class="variety variety--black-honey">BLACK HONEY</div>
    <p class="label__bottom">Pure Australian rare honey from dostwin apiaries, harvested in small batches each season. Net weight 500 g. Product of Australia.</p>
    <div class="label__edge"></div>
  </article>

  <article class="label">
    <div class="label__top"></div>
    <p class="side-copy side-copy--left">Raw honey gathered from native Australian blossoms, cold extracted and unfiltered to keep pollen and enzymes intact.</p>
    <p class="side-copy side-copy--right">Store below 25°C in a dry place. Natural crystallisation may occur; warm gently to restore. Not suitable for infants under twelve months.</p>
    <div class="brand-mark"><span class="brand-mark__dot"></span><span class="brand-mark__name">AUSTRALIA<br>KELUNTO HONEY</span></div>
    <div class="comb" role="img" aria-label="Faint honeycomb pattern behind the title"></div>
    <h2 class="title"><span class="title__brand">Kelunto</span><span class="title__word">Honey</span></h2>
    <svg class="drops" width="24" height="36" viewBox="0 0 24 36" aria-hidden="true"><path d="M6 0 C8 5 10 8 10 11 A4 4 0 0 1 2 11 C2 8 4 5 6 0Z" fill="var(--amber)"/><path d="M16 12 C19 19 22 22 22 27 A6 6 0 0 1 10 27 C10 22 13 19 16 12Z" fill="var(--amber)"/></svg>
    <div class="variety variety--quince">QUINCE</div>
    <p class="label__bottom">Pure Australian rare honey from dostwin apiaries, harvested in small batches each season. Net weight 500 g. Product of Australia.</p>
    <div class="label__edge"></div>
  </article>

</main>
</body>
</html>
```